We specialize in pizza, pasta and salads and are now offering TAKE & BAKE and GRAB & GO ...

Looking for either a 8.5" x 11" or similar for a instore display. WILL BE ON A SWIVELING HOLDER to catch customers attention.

**THIS IS A DOUBLE SIDED PRINT**

ONE SIDE will consist of WHAT'S FOR DINNER TONIGHT? and the following:
* Take & Bake"
* "Baked Pasta"
* Freshly made in house
* Lasagna
$13.50
- please include attached closeup picture and logo

THE OTHER SIDE will consist of
mini charcutier board.
* snack size charcutier delight *
* Enjoy the flavors of gourmet snacking, all in one convenient box!

PRICE $8.99

Winning design will be commissioned to design labels for "grab and go" for take and bake pasta, charcuterie box, pasta salads, candy etc.

Thank you and please do not hesitate to ask any questions.

www.calderipizza.ca
www.fernloop.ca
Logo to be interchanged as they are affiliated meaning FernLoop is a brand within Calderi pizza.

Target Market(s)

our target market is customers who have already entered our business. This is to upsel

Industry/Entity Type

We are in a self serve enviroment and target business people

Requirements
Must have
• must be clean and catchy. We are located in a professional business community.
Nice to have
• Must be appealing, appetizing and utilize our website colors
Should not have
• should not have any carton drawings and not be cluttered (busy)

```html
<!DOCTYPE html>
<html lang="en">
<head>
<meta charset="utf-8">
<title>What's For Dinner Tonight – FernLoop</title>
<link href="https://fonts.googleapis.com/css2?family=Montserrat:wght@500;600;700;800&family=Allura&display=swap" rel="stylesheet">
<style>
  :root {
    --page-bg: #dfe3ea;
    --paper: #f3f0ed;
    --brand-red: #c0301f;
    --ink: #1f1f22;
    --navy: #1b2a4a;
    --headline-grey: #4a4547;
    --pasta-orange: #e0782a;
    --pasta-deep: #b8461c;
    --bowl-rim: #2b2a2c;
    --cheese-gold: #d9a24a;
    --cheese-cream: #f1dfb8;
  }
  * { margin: 0; padding: 0; box-sizing: border-box; }
  html, body { width: 942px; height: 1200px; overflow: hidden; background: var(--page-bg); }
  body { font-family: 'Montserrat', sans-serif; color: var(--ink); }

  .flyer {
    position: absolute; left: 47px; top: 0;
    width: 848px; height: 1200px;
    background: var(--paper);
    overflow: hidden;
  }

  .backdrop-word {
    position: absolute; left: 412px;
    font-family: 'Montserrat', sans-serif; font-weight: 800;
    font-size: 250px; line-height: 1; letter-spacing: -8px;
    color: var(--headline-grey); white-space: nowrap;
  }
  .backdrop-word.w1 { top: 78px; }
  .backdrop-word.w2 { top: 290px; opacity: .35; }
  .backdrop-word.w3 { top: 560px; opacity: .16; }
  .backdrop-word.w4 { top: 830px; opacity: .07; }

  .brand {
    position: absolute; left: 51px; top: 44px; width: 222px;
    text-align: center;
  }
  .brand-dot {
    width: 70px; height: 70px; border-radius: 50%;
    border: 3px solid var(--navy); margin: 0 auto 14px;
  }
  .brand-name {
    font-weight: 600; font-size: 30px; color: var(--navy); letter-spacing: .5px;
  }

  .headline-top {
    position: absolute; left: 51px; top: 226px;
    font-weight: 800; font-size: 48px; letter-spacing: -.5px;
    color: var(--brand-red); line-height: 1;
  }
  .headline-script {
    position: absolute; left: 60px; top: 255px;
    font-family: 'Allura', cursive; font-size: 118px; line-height: 1;
    color: var(--ink);
  }
  .headline-tag {
    position: absolute; left: 137px; top: 341px; width: 226px; height: 70px;
    background: var(--brand-red); color: #fff;
    font-weight: 800; font-size: 42px; line-height: 70px; text-align: center;
  }
  .headline-mark {
    position: absolute; left: 342px; top: 300px;
    font-family: 'Allura', cursive; font-size: 150px; line-height: 1; color: var(--ink);
  }

  .photo-bowl {
    position: absolute; left: 370px; top: 211px; width: 546px; height: 546px;
    border-radius: 50%; border: 20px solid var(--bowl-rim);
    background: radial-gradient(circle at 45% 45%, var(--pasta-orange), var(--pasta-deep) 80%);
    box-shadow: 0 10px 30px rgba(0,0,0,.25);
  }
  .photo-cheese {
    position: absolute; left: 449px; top: 729px; width: 318px; height: 318px;
    border-radius: 50%; border: 1.5px solid var(--brand-red);
    background: radial-gradient(circle at 50% 55%, var(--cheese-cream), var(--cheese-gold) 60%, #8a6a3a);
  }

  .menu-frame {
    position: absolute; left: 49px; top: 484px; width: 366px; height: 576px;
    border: 1.5px solid var(--brand-red);
  }
  .menu-list { position: absolute; left: 72px; list-style: none; }
  .menu-list li {
    display: flex; font-weight: 500; font-size: 21px; line-height: 28px;
    margin-bottom: 12px;
  }
  .menu-list .num {
    width: 44px; flex: none; color: var(--brand-red); font-weight: 600; font-size: 18px;
  }
  .menu-list.dinner { top: 517px; }
  .menu-list.snack { top: 838px; }
  .menu-list.snack li { margin-bottom: 15px; }

  .price {
    position: absolute; width: 131px; height: 57px;
    background: var(--brand-red); color: #fff;
    font-weight: 800; font-size: 33px; line-height: 57px; text-align: center;
    letter-spacing: -.5px;
  }
  .price.dinner { left: 335px; top: 520px; }
  .price.snack { left: 346px; top: 753px; font-size: 35px; }

  .snack-band {
    position: absolute; left: 49px; top: 761px; width: 298px; height: 42px;
    background: var(--ink); color: #fff;
    font-weight: 700; font-size: 15.5px; line-height: 42px; padding-left: 13px;
    white-space: nowrap;
  }

  .footer-brand {
    position: absolute; left: 51px; top: 1108px;
    font-weight: 500; font-size: 38px; letter-spacing: 1px; color: var(--ink);
  }
</style>
</head>
<body>
  <main class="flyer">
    <div class="backdrop-word w1">DINNER</div>
    <div class="backdrop-word w2">DINNER</div>
    <div class="backdrop-word w3">DINNER</div>
    <div class="backdrop-word w4">DINNER</div>

    <header class="brand">
      <div class="brand-dot"></div>
      <div class="brand-name">FernLoop</div>
    </header>

    <h1>
      <span class="headline-top">WHAT'S FOR</span>
      <span class="headline-script">Dinner</span>
      <span class="headline-tag">TONIGHT</span>
      <span class="headline-mark">?</span>
    </h1>

    <div class="photo-bowl" role="img" aria-label="Bowl of baked rigatoni in tomato sauce with basil and parmesan"></div>
    <div class="photo-cheese" role="img" aria-label="Close-up of melted cheese stretching from a baked pasta dish"></div>

    <div class="menu-frame"></div>

    <ul class="menu-list dinner">
      <li><span class="num">01.</span><span>Take &amp; Bake</span></li>
      <li><span class="num">02.</span><span>Baked Pasta</span></li>
      <li><span class="num">03.</span><span>Freshly made<br>in house</span></li>
      <li><span class="num">04.</span><span>Lasagna</span></li>
    </ul>
    <div class="price dinner">$13.50</div>

    <div class="snack-band">MINI CHARCURTERIE BOARD</div>
    <div class="price snack">$8.99</div>

    <ul class="menu-list snack">
      <li><span class="num">01.</span><span>Snack Size<br>Charcutier Delight</span></li>
      <li><span class="num">02.</span><span>Enjoy the flavors of<br>Gourment Snacking,<br>all in one Convenient<br>Box!</span></li>
    </ul>

    <footer class="footer-brand">CALDERI PIZZA</footer>
  </main>
</body>
</html>
```